Maplebrook Self Storage - Business Sign

The sign we are needing designed is our main road sign for our self-storage business. The dimensions of the sign are 57 inches tall x 96 inches wide. We require that our attached logo be on the sign as well as our phone number: 478-216-7745 and website www.MaplebrookStorage.net. Optional information that can be added but not required is our address: 418 Delmont Ridge Pkwy, Ashford Bend, GA 31044.

Industry/Entity Type

Self Storage

Font styles to use
Sans Serif

```html
<!DOCTYPE html>
<html lang="en">
<head>
<meta charset="utf-8">
<title>Maplebrook Self Storage – Road Sign</title>
<link href="https://fonts.googleapis.com/css2?family=Barlow:wght@600;700&display=swap" rel="stylesheet">
<style>
  :root {
    --page: #e6e9ee;
    --sign-white: #ffffff;
    --stripe-light: #e4ebf8;
    --stripe-mid: #cbd8f0;
    --brand-blue: #1f5bb5;
    --panel-grey: #3f3f41;
    --ink-dark: #3a3a3c;
    --text-light: #ffffff;
  }
  * { margin: 0; padding: 0; box-sizing: border-box; }
  html, body { width: 1200px; height: 857px; overflow: hidden; }
  body {
    background: var(--page);
    font-family: "Barlow", Arial, sans-serif;
    position: relative;
  }
  .road-sign {
    position: absolute;
    left: 40px;
    top: 96px;
    width: 1120px;
    height: 665px;
    background: var(--sign-white);
    overflow: hidden;
    box-shadow: 0 10px 30px rgba(0,0,0,0.18);
  }
  .sign-backdrop {
    position: absolute;
    inset: 0;
    background: linear-gradient(180deg, var(--stripe-light) 0%, var(--sign-white) 45%, var(--stripe-mid) 100%);
    opacity: 0.8;
  }
  .brand-name {
    position: absolute;
    left: 0;
    right: 0;
    top: 140px;
    text-align: center;
    color: var(--ink-dark);
    font-weight: 700;
  }
  .brand-name__main {
    display: block;
    font-size: 118px;
    line-height: 1;
  }
  .brand-name__sub {
    display: block;
    font-size: 50px;
    letter-spacing: 0.32em;
    margin-top: 18px;
    padding-left: 0.32em;
  }
  .contact-bands {
    position: absolute;
    left: 0;
    top: 0;
    width: 1120px;
    height: 665px;
  }
  .contact-primary {
    position: absolute;
    left: 62px;
    top: 496px;
    color: var(--text-light);
    font-weight: 700;
  }
  .contact-primary__phone {
    font-size: 80px;
    line-height: 1;
    letter-spacing: 0.02em;
  }
  .contact-primary__web {
    font-size: 27px;
    letter-spacing: 0.06em;
    margin-top: 10px;
    text-transform: uppercase;
  }
  .contact-address {
    position: absolute;
    left: 728px;
    top: 540px;
    color: var(--text-light);
    font-style: normal;
    font-weight: 600;
    font-size: 26px;
    line-height: 1.3;
    letter-spacing: 0.03em;
  }
</style>
</head>
<body>
  <section class="road-sign" aria-label="Maplebrook Self Storage road sign">
    <div class="sign-backdrop" role="img" aria-label="Light blue horizontal stripe pattern background"></div>

    <h1 class="brand-name">
      <span class="brand-name__main">Maplebrook</span>
      <span class="brand-name__sub">SELF STORAGE</span>
    </h1>

    <svg class="contact-bands" viewBox="0 0 1120 665" aria-hidden="true">
      <polygon points="636,492 1120,492 1120,665 694,665" fill="var(--panel-grey)"/>
      <polygon points="0,466 627,466 694,665 0,665" fill="var(--brand-blue)"/>
    </svg>

    <div class="contact-primary">
      <p class="contact-primary__phone">478-216-7745</p>
      <p class="contact-primary__web">www.MaplebrookStorage.net</p>
    </div>

    <address class="contact-address">
      418 Delmont Ridge Pkwy,<br>
      Ashford Bend, GA 31044
    </address>
  </section>
</body>
</html>
```